Ridexa Academy Wordpress Motorcycle School Business Website

We are a motorcycle training school that is located in Calgary, AB, Canada. Our main service is motorcycle safety training. We currently have a site at www.ridexaacademy-example.com . We would like to see a design whereby the colours align with our logo (a white background is best), as well as effectively communicating our strengths as a school and the value and quality of the services we provide.

There are also photos on our facebook page at: www.facebook.com/ridexaacademyexample/ , it would be nice to incorporate some, but we are open to using generic photos as well.

It is important that the entire site be mobile friendly. The front page should be able to house all the information that a potential student would be looking for in terms of WHY they should choose us, without having to navigate to secondary pages.

We also currently have a small youtube clip that we would like to keep on the main page to "hook" a potential customer. We have secondary pages in our menu for further details and also have an integrated booking engine on one of the pages so that student's can book and pay online. These things we would like to keep. It would also be nice to give the ability for our customers to share the website's pages on social media.

Our current subpages are:
About Us
Our Staff
Our Fleet
Client Testimonials
Friends of Ridexa
Course Descriptions
Course Pricing
Bookings (where they book)
FAQ
Privacy Policy
Contact Page

A more efficient and effective method of organizing/delivering the content would be great.

Finally... a sleek, modern/contemporary theme is what we are after. Our company slogan being: Fun - Safe - Professional

Please reference the existing website for all the necessary content.

Target Market(s)

18-50 year old. Motorcycle enthusiast students who want to learn to ride.

Industry/Entity Type

Driving School

Font styles to use
Sans Serif

Requirements
Must have
• Some photos from our facebook page would be great.
• Ridexa Academy Logo colours
• Please refer to the Project Description.
Nice to have
• Modern/Contemporary

```html
<!DOCTYPE html>
<html lang="en">
<head>
<meta charset="utf-8">
<title>Ridexa Academy – Calgary Motorcycle Safety Training School</title>
<link rel="stylesheet" href="https://fonts.googleapis.com/css2?family=Open+Sans:ital,wght@0,400;0,600;0,700;0,800;1,400&family=Oswald:wght@500;700&display=swap">
<style>
:root{
  --yellow:#f6c300;
  --yellow-dark:#d9a900;
  --ink:#2f2f2f;
  --text:#666;
  --muted:#999;
  --line:#e3e3e3;
  --panel:#f3f3f3;
  --blue:#3a77b5;
  --blue-dark:#234f80;
  --footer-base:#3b3300;
}
*{box-sizing:border-box;margin:0;padding:0}
html,body{width:1200px;height:2428px;overflow:hidden;background:#fff}
body{font-family:"Open Sans",Arial,sans-serif;color:var(--text);font-size:12px;position:relative}
.abs{position:absolute}
.btn{display:inline-block;background:var(--yellow);color:var(--ink);font-weight:700;font-size:10px;letter-spacing:.5px;text-transform:uppercase;padding:8px 16px;border-radius:2px;white-space:nowrap}

/* header */
.header{left:0;top:0;width:1200px;height:60px;background:#fff}
.brand{left:40px;top:14px;display:flex;align-items:center;gap:8px}
.brand-mark{width:28px;height:28px;background:var(--yellow)}
.brand-name{font-weight:800;font-size:22px;color:var(--ink)}
.toplinks{right:40px;top:6px;font-size:9px;color:var(--muted);display:flex;gap:14px}
.tagline{left:640px;top:26px;font-size:15px;font-style:italic;color:var(--ink)}
.tagline b{color:var(--yellow-dark);font-style:normal}
.header .btn{right:40px;top:24px;padding:6px 12px}
.nav{left:0;top:60px;width:1200px;height:30px;border-top:1px solid var(--line);border-bottom:3px solid var(--yellow);background:#fff;display:flex;padding-left:40px}
.nav a{font-size:10px;color:var(--ink);padding:0 18px;line-height:27px;text-decoration:none}
.nav a.active{background:var(--yellow);font-weight:700}

/* hero */
.hero{left:0;top:90px;width:1200px;height:310px;background:linear-gradient(180deg,#e9ecef,#cfd3d8);overflow:hidden}
.hero-copy{left:40px;top:40px;width:250px}
.hero-copy h1{font-family:"Oswald",sans-serif;font-size:40px;line-height:40px;color:var(--ink);text-transform:uppercase}
.hero-copy h1 span{color:var(--yellow-dark)}
.hero-copy h2{font-size:14px;font-weight:700;color:var(--ink);margin-top:8px}
.hero-copy p{font-size:10px;line-height:15px;margin:10px 0 18px;color:#555}
.hero-video{left:290px;top:20px;width:360px;height:270px;border-radius:40px;background:radial-gradient(circle at 50% 50%,#ffffff,#e2e6ea)}
.video-bar{left:350px;top:238px;width:260px;height:22px;background:#222;opacity:.85}
.rider{left:650px;top:0;width:550px;height:310px;background:linear-gradient(135deg,#7e8a96,#a6b0b8 50%,#6f6a5f)}
.arrow-btn{width:26px;height:40px;background:rgba(0,0,0,.45);display:flex;align-items:center;justify-content:center}

/* pricing */
.pricing{left:0;top:400px;width:1200px;height:560px;background:var(--panel)}
.card{top:90px;width:215px;height:440px;background:#fff;border-top:4px solid var(--yellow);text-align:center;padding:26px 20px}
.card.featured{top:70px;height:480px;border:4px solid var(--yellow);box-shadow:0 6px 18px rgba(0,0,0,.12)}
.card h3{font-size:11px;font-weight:600;color:var(--muted);text-transform:uppercase;letter-spacing:1px}
.card.featured h3{color:var(--yellow-dark)}
.price{font-size:44px;font-weight:300;color:var(--yellow-dark);margin:14px 0 4px}
.price sup{font-size:16px}
.card hr{border:0;border-top:1px solid var(--line);margin:14px 0}
.card li{list-style:none;font-size:10px;line-height:22px;color:var(--text)}
.card .btn{position:absolute;left:50%;bottom:30px;transform:translateX(-50%)}

/* fleet */
.section-title{font-family:"Oswald",sans-serif;font-size:15px;color:var(--ink);text-transform:uppercase;display:flex;align-items:center;gap:12px}
.section-title::after{content:"";flex:1;height:1px;background:var(--line)}
.fleet-title{left:200px;top:1000px;width:800px}
.bike{top:1040px;width:250px}
.bike-photo{height:150px;background:radial-gradient(ellipse at 50% 60%,#9aa0a6,#ffffff 70%)}
.bike h4{font-size:13px;font-weight:700;color:var(--ink);margin:18px 0 8px;text-transform:uppercase}
.bike p{font-size:10px;line-height:15px}

/* team */
.team{left:0;top:1340px;width:1200px;height:240px;background:linear-gradient(100deg,var(--blue-dark),var(--blue) 55%,#5a93c9)}
.team-title{left:200px;top:16px;color:#fff;font-family:"Oswald",sans-serif;font-size:15px;text-transform:uppercase}
.member{top:70px;width:120px;height:130px;background:linear-gradient(160deg,#5c6670,#2c3238)}
.member.highlight{top:60px;height:150px;background:var(--yellow);text-align:center;padding-top:20px}
.member.highlight .avatar{width:60px;height:60px;border-radius:50%;background:#fff;margin:0 auto 10px}
.member.highlight b{display:block;font-size:11px;color:var(--ink)}
.member.highlight span{font-size:9px;color:var(--ink)}

/* why + testimonial */
.why{left:200px;top:1610px;width:380px}
.why ul{margin-top:22px}
.why li{list-style:none;display:flex;gap:10px;font-size:11px;line-height:15px;margin-bottom:17px}
.tick{flex:none;width:15px;height:15px;border-radius:50%;background:var(--yellow);display:flex;align-items:center;justify-content:center}
.testimonial{left:620px;top:1610px;width:380px}
.quote{margin-top:22px;background:var(--panel);padding:22px;font-size:11px;line-height:18px;position:relative}
.quote::after{content:"";position:absolute;left:30px;bottom:-12px;border:12px solid transparent;border-top-color:var(--panel);border-bottom:0}
.author{margin-top:24px;display:flex;align-items:center;gap:10px;font-size:11px}
.author i{width:36px;height:36px;border-radius:50%;background:#bdbdbd;display:block}

/* cta */
.cta{left:200px;top:1880px;width:800px;height:80px;border:1px solid var(--line);border-left:5px solid var(--yellow);background:#fff;display:flex;align-items:center;justify-content:space-between;padding:0 30px}
.cta p{font-size:14px;color:var(--ink);line-height:20px}
.cta small{display:block;font-size:10px;color:var(--text)}

/* footer */
.footer{left:0;top:1996px;width:1200px;height:408px;background:var(--yellow)}
.fcol{top:48px;font-size:11px;line-height:17px;color:var(--footer-base)}
.fcol h5{font-size:11px;font-weight:700;text-transform:uppercase;margin-bottom:14px;color:var(--ink)}
.fcol li{list-style:none;border-bottom:1px solid rgba(0,0,0,.12);padding:7px 0}
.fcol p + p{margin-top:14px}
.socials{display:flex;gap:8px;margin-top:18px}
.socials i{width:22px;height:22px;border-radius:50%;background:var(--ink);display:block}
.badges{display:grid;grid-template-columns:repeat(3,52px);gap:8px}
.badges i{height:36px;background:#fff;display:block}
.footer-rule{left:200px;top:330px;width:800px;height:1px;background:rgba(0,0,0,.15)}
.footer-bottom{left:200px;top:350px;width:800px;display:flex;justify-content:space-between;align-items:center;font-size:11px;color:var(--footer-base)}
.footer-bottom .socials{margin-top:0}
.footer-bottom .socials i{width:18px;height:18px}
.bottom-bar{left:0;top:2404px;width:1200px;height:24px;background:var(--yellow-dark);font-size:9px;color:var(--footer-base);padding:6px 200px}
</style>
</head>
<body>

<header class="abs header">
  <div class="abs brand"><span class="brand-mark"></span><span class="brand-name">Ridexa</span></div>
  <div class="abs toplinks"><span>Friends of Ridexa</span><span>FAQ</span><span>Privacy Policy</span></div>
  <div class="abs tagline">Fun <b>·</b> Safe <b>·</b> Professional</div>
  <span class="abs btn">Book a class now</span>
</header>
<nav class="abs nav">
  <a class="active">Home</a><a>About Us</a><a>Our Team</a><a>Our Fleet</a><a>Courses</a><a>Prices</a><a>Booking</a><a>Testimonials</a><a>Contact</a>
</nav>

<section class="abs hero">
  <div class="abs rider" role="img" aria-label="Photo of a rider in full gear on a sport motorcycle"></div>
  <div class="abs hero-video" role="img" aria-label="Promotional video frame showing a school motorcycle"></div>
  <div class="abs video-bar"></div>
  <svg class="abs" style="left:450px;top:125px" width="60" height="60" viewBox="0 0 60 60"><circle cx="30" cy="30" r="28" fill="rgba(0,0,0,.55)"/><path d="M24 18 L42 30 L24 42Z" fill="#fff"/></svg>
  <div class="abs hero-copy">
    <h1>Fun <span>Safe</span><br>Professional</h1>
    <h2>Calgary Motorcycle Safety Training School</h2>
    <p>Learn to ride with certified instructors, modern bikes and small class sizes. Build real confidence on the road from your very first lesson.</p>
    <span class="btn">Book now</span>
  </div>
  <div class="abs arrow-btn" style="left:0;top:135px"><svg width="10" height="14"><path d="M8 1 L2 7 L8 13" stroke="#fff" stroke-width="2" fill="none"/></svg></div>
  <div class="abs arrow-btn" style="right:0;top:135px"><svg width="10" height="14"><path d="M2 1 L8 7 L2 13" stroke="#fff" stroke-width="2" fill="none"/></svg></div>
</section>

<section class="abs pricing">
  <div class="abs card" style="left:195px">
    <h3>Basic</h3><div class="price">$599<sup>.00</sup></div><hr>
    <ul><li>Full beginner training</li><li>Use of school bike</li><li>Gear provided</li><li>Road test preparation</li></ul>
    <span class="btn">View more</span>
  </div>
  <div class="abs card" style="left:418px">
    <h3>Refresher</h3><div class="price">$449<sup>.00</sup></div><hr>
    <ul><li>For returning riders</li><li>Skill assessment</li><li>Use of school bike</li><li>Traffic practice</li></ul>
    <span class="btn">View more</span>
  </div>
  <div class="abs card featured" style="left:625px">
    <h3>Professional</h3><div class="price">$399<sup>.00</sup></div><hr>
    <ul><li>Advanced riding skills</li><li>Emergency braking drills</li><li>Cornering technique</li><li>Personal coaching</li></ul>
    <span class="btn">View more</span>
  </div>
  <div class="abs card" style="left:850px">
    <h3>Repeat</h3><div class="price">$299<sup>.00</sup></div><hr>
    <ul><li>Repeat any course</li><li>Same great instructors</li><li>Flexible schedule</li><li>Use of school bike</li></ul>
    <span class="btn">View more</span>
  </div>
</section>

<h3 class="abs section-title fleet-title">Our Fleet</h3>
<div class="abs bike" style="left:200px">
  <div class="bike-photo" role="img" aria-label="Photo of a white and red sport motorcycle"></div>
  <h4>Kaiden KR125</h4>
  <p>A light, forgiving sport bike ideal for new riders. Smooth power delivery and easy handling help students learn control quickly.</p>
</div>
<div class="abs bike" style="left:475px">
  <div class="bike-photo" role="img" aria-label="Photo of a black cruiser motorcycle"></div>
  <h4>Sorai SZ250</h4>
  <p>A low seat cruiser with relaxed ergonomics. Perfect for riders who want a stable, comfortable bike while mastering the basics.</p>
</div>
<div class="abs bike" style="left:750px">
  <div class="bike-photo" role="img" aria-label="Photo of a red and black sport motorcycle"></div>
  <h4>Kaiden KR250</h4>
  <p>A capable step-up bike for refresher and advanced courses. Responsive brakes and agile handling for confident progression.</p>
</div>

<section class="abs team">
  <h3 class="abs team-title">Meet Our Team</h3>
  <div class="abs member" style="left:230px" role="img" aria-label="Photo of an instructor in a helmet"></div>
  <div class="abs member highlight" style="left:400px"><div class="avatar"></div><b>Lead Instructor</b><span>Senior Coach</span></div>
  <div class="abs member" style="left:540px" role="img" aria-label="Photo of an instructor on a motorcycle"></div>
  <div class="abs member" style="left:680px" role="img" aria-label="Photo of an instructor at the training lot"></div>
  <div class="abs member" style="left:820px" role="img" aria-label="Photo of an instructor in riding gear"></div>
  <div class="abs arrow-btn" style="left:180px;top:100px;background:var(--yellow)"><svg width="10" height="14"><path d="M8 1 L2 7 L8 13" stroke="#333" stroke-width="2" fill="none"/></svg></div>
  <div class="abs arrow-btn" style="left:994px;top:100px;background:var(--yellow)"><svg width="10" height="14"><path d="M2 1 L8 7 L2 13" stroke="#333" stroke-width="2" fill="none"/></svg></div>
</section>

<section class="abs why">
  <h3 class="section-title">Why Choose Us</h3>
  <ul>
    <li><span class="tick"><svg width="8" height="8"><path d="M1 4 L3 6 L7 1" stroke="#fff" stroke-width="1.6" fill="none"/></svg></span>Certified instructors with years of riding experience</li>
    <li><span class="tick"><svg width="8" height="8"><path d="M1 4 L3 6 L7 1" stroke="#fff" stroke-width="1.6" fill="none"/></svg></span>Small class sizes for more personal attention</li>
    <li><span class="tick"><svg width="8" height="8"><path d="M1 4 L3 6 L7 1" stroke="#fff" stroke-width="1.6" fill="none"/></svg></span>Modern, well maintained school motorcycles</li>
    <li><span class="tick"><svg width="8" height="8"><path d="M1 4 L3 6 L7 1" stroke="#fff" stroke-width="1.6" fill="none"/></svg></span>All safety gear included with every course</li>
    <li><span class="tick"><svg width="8" height="8"><path d="M1 4 L3 6 L7 1" stroke="#fff" stroke-width="1.6" fill="none"/></svg></span>Flexible weekday and weekend schedules</li>
    <li><span class="tick"><svg width="8" height="8"><path d="M1 4 L3 6 L7 1" stroke="#fff" stroke-width="1.6" fill="none"/></svg></span>Easy online booking and secure payment</li>
    <li><span class="tick"><svg width="8" height="8"><path d="M1 4 L3 6 L7 1" stroke="#fff" stroke-width="1.6" fill="none"/></svg></span>Road test preparation built into every course</li>
  </ul>
</section>
<section class="abs testimonial">
  <h3 class="section-title">What Our Client Say</h3>
  <div class="quote">I had never ridden before and felt nervous, but the instructors were patient and encouraging from start to finish. The course was well organized, the bikes were great and I passed my road test on the first try. I would recommend this school to anyone who wants to learn to ride safely.</div>
  <div class="author"><i></i><span><b>Happy Student</b> – Calgary</span></div>
</section>

<div class="abs cta">
  <p>We are Ridexa Academy! Have questions about our classes?<small>Call us at 403-555-0148 or email info@ridexaacademy-example.com</small></p>
  <span class="btn">Contact us</span>
</div>

<footer class="abs footer">
  <div class="abs fcol" style="left:200px;width:180px">
    <div style="display:flex;align-items:center;gap:8px;margin-bottom:14px"><span style="width:24px;height:24px;background:var(--ink);display:block"></span><b style="font-size:20px;color:var(--ink);font-weight:800">Ridexa</b></div>
    <p>Calgary motorcycle safety training for new and returning riders. Fun, safe and professional courses all season long.</p>
    <p>Call 403-555-0148<br>info@ridexaacademy-example.com</p>
  </div>
  <div class="abs fcol" style="left:410px;width:170px">
    <h5>Recent Posts</h5>
    <ul><li>Preparing for your first lesson</li><li>Choosing the right riding gear</li><li>Spring season tips for riders</li><li>Road test checklist explained</li><li>Staying visible in traffic</li></ul>
  </div>
  <div class="abs fcol" style="left:610px;width:170px">
    <h5>Latest Updates</h5>
    <p>New summer class dates are now open for booking. Reserve your spot early.</p>
    <p>Congratulations to all students who passed their road test this week.</p>
    <p>Weekend refresher sessions return next month.</p>
  </div>
  <div class="abs fcol" style="left:820px;width:180px">
    <h5>Friends of Ridexa</h5>
    <div class="badges"><i></i><i></i><i></i><i></i><i></i><i></i></div>
  </div>
  <div class="abs footer-rule"></div>
  <div class="abs footer-bottom"><span>Fun · Safe · Professional</span><div class="socials"><i></i><i></i><i></i><i></i><i></i></div></div>
</footer>
<div class="abs bottom-bar">© Ridexa Academy. All Rights Reserved.</div>

</body>
</html>
```